we need a business card in yellow, green and black with rounded edges. We are in the Construction and Engineering business. I need the below info included:

Neil Barton
Bluestone Engineering & Construction, Inc.
4168 Harbor Crest Road,
Santa Ana, Ca 92814
714-555-0147 Office
714-555-0192 Cell
714-555-0163 Fax
nb@bluestonexq.example

thanks for your help!

```html
<!DOCTYPE html>
<html lang="en">
<head>
<meta charset="utf-8">
<title>Bluestone Engineering &amp; Construction – Business Card</title>
<link href="https://fonts.googleapis.com/css2?family=Alike&family=Gentium+Book+Plus&display=swap" rel="stylesheet">
<style>
  :root {
    --page: #ffffff;
    --card: #e4dcab;
    --green: #0b4a12;
    --green-line: #2f6b2a;
    --ink: #111111;
  }
  html, body {
    margin: 0;
    padding: 0;
    width: 1200px;
    height: 1000px;
    overflow: hidden;
    background: var(--page);
  }
  .business-card {
    position: absolute;
    left: 295px;
    top: 307px;
    width: 660px;
    height: 387px;
    border-radius: 18px;
    background: var(--card);
    border-left: 3px solid var(--green);
    box-sizing: border-box;
    overflow: hidden;
  }
  .company-name {
    position: absolute;
    left: 11px;
    top: 18px;
    margin: 0;
    font-family: "Alike", serif;
    font-weight: 400;
    font-size: 31px;
    line-height: 1;
    color: var(--green);
    white-space: nowrap;
  }
  .company-address {
    position: absolute;
    left: 11px;
    top: 61px;
    margin: 0;
    font-family: "Alike", serif;
    font-weight: 700;
    font-size: 15px;
    line-height: 1;
    color: var(--green);
    white-space: nowrap;
  }
  .person-name {
    position: absolute;
    left: 11px;
    top: 170px;
    width: 306px;
    margin: 0;
    padding-bottom: 4px;
    border-bottom: 1px solid var(--green-line);
    font-family: "Gentium Book Plus", serif;
    font-weight: 400;
    font-size: 38px;
    letter-spacing: 1px;
    line-height: 1.05;
    color: var(--ink);
  }
  .contact-list {
    position: absolute;
    left: 11px;
    top: 221px;
    margin: 0;
    padding: 0;
    list-style: none;
    font-family: "Gentium Book Plus", serif;
    font-size: 19.5px;
    letter-spacing: 1px;
    line-height: 26px;
    color: var(--ink);
  }
  .corner-emblem {
    position: absolute;
    right: 0;
    bottom: 0;
    width: 175px;
    height: 169px;
    display: block;
  }
</style>
</head>
<body>
  <article class="business-card">
    <h1 class="company-name">Bluestone Engineering &amp; Construction, Inc.</h1>
    <p class="company-address">4168 Harbor Crest Road,Santa Ana, Ca 92814</p>

    <h2 class="person-name">Neil Barton</h2>
    <ul class="contact-list">
      <li>Office 714-555-0147</li>
      <li>Cell 714-555-0192</li>
      <li>Fax 714-555-0163</li>
      <li>Email nb@bluestonexq.example</li>
    </ul>

    <svg class="corner-emblem" viewBox="0 0 175 169" role="img" aria-label="Company emblem area (green corner decoration)">
      <defs>
        <radialGradient id="emblem-fill" cx="1" cy="1" r="1">
          <stop offset="0" stop-color="#0b4a12" stop-opacity="0.85"/>
          <stop offset="1" stop-color="#0b4a12" stop-opacity="0.15"/>
        </radialGradient>
      </defs>
      <rect x="0" y="0" width="175" height="169" fill="url(#emblem-fill)"/>
    </svg>
  </article>
</body>
</html>
```